Website design for an existing website that is currently live.

The website is vrolpworkshops.com and this will be the easiest design you will ever do because he LOVES his existing website and I convinced him to "modernize it" a bit. That means that it's not a from scratch design. All I need is to take the existing design and modify it to be more up to date with current design trends. To make it easier, I also have the original psd file from 2016 that I included in the project. For deails, it's really easy. Go to vrolpworkshops.com and use the same navigation, links, highlighted areas etc.. it's ok to move them around etc but it must contain all the current links because it's going to replace a live site. I will need a home page design and a simplified inner page design that I can use to plug in the content.

```html
<!DOCTYPE html>
<html lang="en">
<head>
<meta charset="utf-8">
<title>VROLPWORKSHOPS – Online Chiropractic CE</title>
<link rel="stylesheet" href="https://fonts.googleapis.com/css2?family=Poppins:wght@400;500;600;700&family=Lato:wght@400;700&display=swap">
<style>
:root{
  --blue:#0b5bd3;
  --blue-bright:#1466e0;
  --navy:#0f2a66;
  --deep:#0b2f7c;
  --ink:#1c1c1c;
  --muted:#555b66;
  --gray:#edf0f5;
  --line:#d9dde4;
  --white:#ffffff;
}
*{box-sizing:border-box;margin:0;padding:0}
html,body{width:1200px;height:4216px;overflow:hidden}
body{font-family:"Lato",sans-serif;color:var(--ink);background:var(--white);position:relative}
h1,h2,h3,h4,.btn,.nav a{font-family:"Poppins",sans-serif}
section,header,footer{position:relative;width:1200px}
.abs{position:absolute}

/* top bar + header */
.topbar{position:absolute;top:0;right:0;width:430px;height:30px;background:var(--blue);border-bottom-left-radius:14px;display:flex;align-items:center;gap:34px;padding-left:42px;z-index:2}
.topbar a{color:var(--white);font:500 11px "Poppins",sans-serif;text-decoration:none;letter-spacing:.3px}
.site-header{height:102px}
.brand{position:absolute;left:122px;top:14px;display:flex;align-items:center;gap:10px;text-decoration:none}
.brand-dot{width:48px;height:48px;border-radius:50%;background:var(--blue)}
.brand-name{font:700 19px "Poppins",sans-serif;color:var(--navy);line-height:1}
.nav{position:absolute;left:366px;top:56px;display:flex;gap:37px}
.nav a{font-size:12px;color:var(--ink);text-decoration:none;letter-spacing:.3px}
.nav a.active{font-weight:600}
.cart{position:absolute;left:1045px;top:50px}

/* hero */
.hero{height:540px;overflow:hidden}
.hero-photo{position:absolute;inset:0;background:linear-gradient(100deg,#f1f1ef 0%,#e4e6e2 40%,#b9c3b4 62%,#6d7d67 78%,#dfe2dc 100%)}
.hero-curve{position:absolute;right:0;bottom:0}
.hero-badge{position:absolute;left:80px;top:48px;width:420px;height:420px;border-radius:50%;background:radial-gradient(circle at 40% 35%,#1d5cc6,#103d9a);box-shadow:0 0 0 4px rgba(255,255,255,.9),0 0 0 6px #1a4fb3;text-align:center;color:var(--white);padding-top:124px}
.hero-badge p{font:400 20px "Poppins",sans-serif}
.hero-badge h1{font:700 30px/1.35 "Poppins",sans-serif;margin-top:12px}
.btn{display:inline-block;font-weight:600;font-size:13px;letter-spacing:1px;text-transform:uppercase;text-decoration:none;border-radius:22px;text-align:center}
.btn-outline{border:2px solid var(--white);color:var(--white);width:166px;height:42px;line-height:38px;margin-top:26px}
.btn-white{background:var(--white);color:var(--blue);width:178px;height:42px;line-height:42px}
.btn-blue{background:var(--blue);color:var(--white);width:178px;height:42px;line-height:42px}

/* search */
.search-band{height:128px;background:var(--blue)}
.field{position:absolute;top:41px;height:42px;background:var(--blue);border:1px solid rgba(255,255,255,.85);color:var(--white);font-size:12px;padding:0 16px;display:flex;align-items:center;justify-content:space-between}
.search-btn{position:absolute;left:925px;top:41px;width:141px;height:42px;background:var(--navy);color:var(--white);font:600 14px "Poppins",sans-serif;display:flex;align-items:center;justify-content:center;gap:6px}

/* steps */
.steps-wrap{height:442px;background:linear-gradient(var(--blue) 50%,var(--gray) 50%)}
.steps{position:absolute;inset:0;background:var(--white);border-radius:180px 0 190px 0}
.section-title{font:400 29px "Poppins",sans-serif;text-align:center;color:var(--ink)}
.section-title strong{font-weight:700}
.rule{width:70px;height:3px;background:var(--blue);margin:14px auto 0}
.step{position:absolute;width:260px;text-align:center}
.step h3{font:600 15px "Poppins",sans-serif;color:var(--navy);margin-top:14px}
.step p{font-size:12px;line-height:1.75;color:var(--muted);margin-top:6px}

/* free class */
.free{height:540px;background:var(--gray)}
.free-frame{position:absolute;left:111px;top:81px;width:240px;height:200px;background:var(--blue)}
.free-photo{position:absolute;left:126px;top:94px;width:485px;height:344px;background:linear-gradient(120deg,#3c5f8f,#cfd6df 45%,#e9e3d7 60%,#8a8f97);border-radius:0 70px 0 60px}
.free-text{position:absolute;left:670px;top:122px;width:470px}
.free-text h2{font:400 30px/1.2 "Poppins",sans-serif}
.free-text h2 strong{font-weight:700}
.free-text .rule{margin:12px 0 0}
.free-text p{font-size:13px;line-height:2.2;color:#3f444c;margin-top:30px}
.free-text a{color:var(--ink);font-weight:700}

/* choice */
.choice-wrap{height:507px;background:linear-gradient(var(--white) 50%,var(--navy) 50%)}
.choice{position:absolute;inset:0;background:var(--white);border-radius:0 0 0 80px;overflow:hidden}
.choice-photo{position:absolute;left:622px;top:0;width:578px;height:507px;background:linear-gradient(120deg,#6a5a47,#b49a80 40%,#d8cbbb 60%,#4f5a45)}
.choice-text{position:absolute;left:120px;top:62px;width:430px}
.choice-text h2{font:700 25px/1.45 "Poppins",sans-serif}
.choice-text .rule{margin:18px 0 0}
.choice-text h4{font:600 15px "Poppins",sans-serif;margin:28px 0 0 4px}
.choice-text p{font-size:12px;line-height:2.3;color:var(--muted);margin-top:14px}
.choice-text .btn{margin-top:18px}

/* bundle */
.bundle{height:503px;background:linear-gradient(115deg,#123a8c 0%,#0c2a6a 45%,#0e2456 100%);color:var(--white);text-align:center}
.bundle-bg{position:absolute;inset:0;background:radial-gradient(ellipse at 30% 70%,rgba(110,150,220,.35),transparent 55%),radial-gradient(ellipse at 88% 45%,rgba(140,170,220,.25),transparent 40%)}
.bundle-inner{position:absolute;left:0;right:0;top:125px}
.bundle h2{font:700 29px "Poppins",sans-serif}
.bundle h3{font:400 24px "Poppins",sans-serif;margin-top:2px}
.bundle p{width:790px;margin:34px auto 0;font-size:14px;line-height:1.95}
.bundle .btn{margin-top:28px}

/* certificates */
.certs-wrap{height:700px;background:linear-gradient(var(--navy) 50%,var(--deep) 50%)}
.certs{position:absolute;inset:0;background:var(--white);border-radius:0 180px 0 110px}
.certs .section-title{position:absolute;top:68px;left:0;right:0;line-height:1.25}
.card{position:absolute;width:284px;height:221px;border:2px solid var(--line);text-align:center;display:flex;flex-direction:column;align-items:center;justify-content:center;gap:20px}
.card.featured{background:var(--blue);border-color:var(--blue);color:var(--white)}
.card h4{font:600 15px/1.6 "Poppins",sans-serif}
.card .ico{width:80px;height:80px;border-radius:50%;background:var(--white);box-shadow:0 4px 14px rgba(20,70,160,.18);display:flex;align-items:center;justify-content:center}

/* certificate program */
.program{height:410px;background:linear-gradient(100deg,#0c2f86 0%,#0a4ec8 55%,#0d5fe0 100%);text-align:center;color:var(--white)}
.program-bg{position:absolute;inset:0;background:radial-gradient(ellipse at 20% 60%,rgba(255,255,255,.08),transparent 45%)}
.program h2{position:absolute;top:120px;left:0;right:0;font:400 32px "Poppins",sans-serif}
.program h2 strong{font-weight:700}
.program p{position:absolute;top:182px;left:250px;width:700px;font:400 19px/1.4 "Poppins",sans-serif}
.program .btn{position:absolute;top:262px;left:525px}

/* footer */
.footer{height:344px;background:var(--navy);color:var(--white)}
.footer h4{font:500 16px "Poppins",sans-serif}
.footer .mini{width:30px;height:2px;background:var(--white);margin-top:8px}
.f-contact{position:absolute;left:143px;top:54px}
.f-contact p{font-size:12px;margin-top:26px;color:#d9e1f2}
.f-contact .phone{font:600 16px "Poppins",sans-serif;color:var(--white);margin-top:14px}
.f-links{position:absolute;left:491px;top:48px}
.f-links ul{list-style:none;display:grid;grid-template-columns:172px 140px;row-gap:16px;margin-top:24px;margin-left:6px}
.f-links a{font-size:12px;color:#d9e1f2;text-decoration:none}
.login{position:absolute;left:797px;top:0;width:243px;height:234px;background:#0b2459;border-radius:0 0 18px 18px;padding:38px 28px 0}
.login input{display:block;width:194px;height:28px;border:1px solid #c8d4ee;border-radius:14px;background:transparent;color:var(--white);font-size:10px;padding:0 14px;margin-top:14px}
.login .mini{margin-bottom:12px}
.login button{display:block;width:194px;height:28px;margin-top:16px;border:0;border-radius:14px;background:var(--blue);color:var(--white);font:600 11px "Poppins",sans-serif;letter-spacing:1px}
.login a{display:block;text-align:center;font-size:9px;color:var(--white);margin-top:8px;font-weight:700}
.copyright{position:absolute;left:0;right:0;top:314px;text-align:center;font-size:10px;color:#9aa8c7}
</style>
</head>
<body>

<div class="topbar"><a href="#">TESTIMONIALS</a><a href="#">CONTACT US</a><a href="#">LOGIN</a></div>

<header class="site-header">
  <a class="brand" href="#"><span class="brand-dot"></span><span class="brand-name">VROLPWORKSHOPS</span></a>
  <nav class="nav">
    <a class="active" href="#">COURSES</a><a href="#">CERTIFICATION PROGRAMS</a><a href="#">MEET THE FACULTY</a><a href="#">FAQS</a><a href="#">STATE APPROVALS</a>
  </nav>
  <svg class="cart" width="32" height="30" viewBox="0 0 32 30" fill="none" stroke="#0b5bd3" stroke-width="2.4" stroke-linecap="round" stroke-linejoin="round"><path d="M2 3h5l4 16h15l3-11H9"/><circle cx="13" cy="25" r="2"/><circle cx="24" cy="25" r="2"/></svg>
</header>

<section class="hero">
  <div class="hero-photo" role="img" aria-label="Chiropractor at a desk studying on a laptop beside a green desk lamp"></div>
  <svg class="hero-curve" width="560" height="150" viewBox="0 0 560 150"><path d="M0 150 C180 150 420 120 560 0 L560 150 Z" fill="#0b5bd3"/></svg>
  <div class="hero-badge">
    <p>Online Chiropractic CE Available</p>
    <h1>24/7 From Home,<br>Office Or On The Go!</h1>
    <a class="btn btn-outline" href="#">Get Started</a>
  </div>
</section>

<section class="search-band">
  <div class="field" style="left:133px;width:253px">Course Format <svg width="14" height="8" viewBox="0 0 14 8"><path d="M1 1l6 6 6-6" stroke="#fff" stroke-width="2" fill="none"/></svg></div>
  <div class="field" style="left:395px;width:253px">Topic <svg width="14" height="8" viewBox="0 0 14 8"><path d="M1 1l6 6 6-6" stroke="#fff" stroke-width="2" fill="none"/></svg></div>
  <div class="field" style="left:657px;width:253px">CE Hours <svg width="14" height="8" viewBox="0 0 14 8"><path d="M1 1l6 6 6-6" stroke="#fff" stroke-width="2" fill="none"/></svg></div>
  <div class="search-btn"><svg width="14" height="14" viewBox="0 0 14 14"><circle cx="6" cy="6" r="4.5" stroke="#fff" stroke-width="2" fill="none"/><path d="M9.5 9.5L13 13" stroke="#fff" stroke-width="2"/></svg>SEARCH</div>
</section>

<section class="steps-wrap">
  <div class="steps">
    <h2 class="section-title" style="position:absolute;top:64px;left:0;right:0">How to Get <strong>Start Online Class</strong></h2>
    <div class="rule" style="position:absolute;top:108px;left:565px;margin:0"></div>
    <svg class="abs" style="left:320px;top:158px" width="560" height="60" viewBox="0 0 560 60" fill="none" stroke="#9fbfe8" stroke-width="1.5" stroke-dasharray="4 5"><path d="M12 40 C90 -4 180 8 220 24"/><path d="M340 40 C400 70 470 50 540 20"/></svg>
    <div class="step" style="left:152px;top:148px">
      <svg width="150" height="110" viewBox="0 0 150 110" fill="none" stroke="#8db6ea" stroke-width="2"><text x="10" y="92" font-family="Poppins" font-size="90" font-weight="600" fill="none" stroke="#8db6ea">1</text><circle cx="90" cy="50" r="48"/><rect x="76" y="32" width="28" height="36" rx="3" stroke="#0b5bd3"/><path d="M82 42h16M82 50h16M82 58h10" stroke="#0b5bd3"/></svg>
      <h3>CLICK COURSE FORMAT</h3><p>Choose Online, Webinar<br>or Seminar</p>
    </div>
    <div class="step" style="left:481px;top:148px">
      <svg width="150" height="110" viewBox="0 0 150 110" fill="none" stroke="#8db6ea" stroke-width="2"><text x="6" y="92" font-family="Poppins" font-size="90" font-weight="600" fill="none" stroke="#8db6ea">2</text><circle cx="90" cy="50" r="48"/><path d="M86 36v22l-5-4-4 3 10 12h14l3-14-11-3v-16a3.5 3.5 0 0 0-7 0z" stroke="#0b5bd3"/></svg>
      <h3>CLICK ON TOPIC</h3><p>Choose a Topic from Bullet Proof<br>Documentation to Whiplash</p>
    </div>
    <div class="step" style="left:820px;top:148px">
      <svg width="150" height="110" viewBox="0 0 150 110" fill="none" stroke="#8db6ea" stroke-width="2"><text x="6" y="92" font-family="Poppins" font-size="90" font-weight="600" fill="none" stroke="#8db6ea">3</text><circle cx="90" cy="50" r="48"/><circle cx="86" cy="46" r="12" stroke="#0b5bd3"/><path d="M95 55l12 12" stroke="#0b5bd3" stroke-width="3"/></svg>
      <h3>CLICK ON SEARCH</h3><p>You will then see a list of courses<br>to choose from.</p>
    </div>
  </div>
</section>

<section class="free">
  <div class="free-frame"></div>
  <div class="free-photo" role="img" aria-label="Chiropractor showing a spine model to a patient"></div>
  <div class="free-text">
    <h2>Try Our Free Online<br><strong>Chiropractic Class</strong></h2>
    <div class="rule"></div>
    <p>If you have never taken an online course, we suggest starting with our free 1 hour program in Coding &amp; Documentation. By taking this course you will obtain a true sample of just how easy it is to take one of our courses and receive CE credit (approved in most states).</p>
    <p style="margin-top:20px;font-weight:700;color:var(--ink)">Please click <a href="#">HERE</a> to try Online Chiropractic CE for free!</p>
  </div>
</section>

<section class="choice-wrap">
  <div class="choice">
    <div class="choice-text">
      <h2>Get Chiropractic CEU Credit Hours Online through Recorded Courses or&nbsp; Live Webinars.</h2>
      <div class="rule"></div>
      <h4>What could be better than having a choice?</h4>
      <p>At VROLPWORKSHOPS you have a choice. We have online chiropractic CE courses available 24/7 or live webinars! Imagine, now you can take CE classes at home, at the office, or on the go. Our online CE classes</p>
      <a class="btn btn-blue" href="#">Learn More</a>
    </div>
    <div class="choice-photo" role="img" aria-label="Student smiling while studying on a laptop beside a plant"></div>
  </div>
</section>

<section class="bundle">
  <div class="bundle-bg" role="img" aria-label="Blue-toned photo of hands typing on a laptop"></div>
  <div class="bundle-inner">
    <h2>The More Courses You Take, The More You Save!</h2>
    <h3>Now You Can Bundle Webinars &amp; Recorded Classes!</h3>
    <p>If You Purchase 6-9 Hours Use Promo Code “6hbc” During Check Out &amp; Save 10%. This Offer Applies To Live Webinars &amp; Recorded Online Classes. If You Purchase 10 Hours or More Use Promo Code “10hbc” During Check Out &amp; Save 20%. This Offer Applies To Live Webinars &amp; Recorded Online Classes.</p>
    <a class="btn btn-blue" href="#">Get Started</a>
  </div>
</section>

<section class="certs-wrap">
  <div class="certs">
    <h2 class="section-title">Certified Chiropractic<br><strong>Specialty Programs Are NOW Available:</strong></h2>
    <div class="rule" style="position:absolute;top:166px;left:555px;margin:0"></div>

    <div class="card featured" style="left:146px;top:171px">
      <span class="ico"><svg width="40" height="40" viewBox="0 0 40 40" fill="none" stroke="#0b5bd3" stroke-width="2"><path d="M20 6c-8 0-14 5-14 13 0 7 5 13 14 15 9-2 14-8 14-15 0-8-6-13-14-13zM20 6v28M12 14c3 1 5 4 5 7M28 14c-3 1-5 4-5 7"/></svg></span>
      <h4>48 Hour Chiropractic<br>Neurology Certificate</h4>
    </div>
    <div class="card" style="left:445px;top:171px">
      <span class="ico"><svg width="40" height="40" viewBox="0 0 40 40" fill="none" stroke="#0b5bd3" stroke-width="2"><path d="M8 14h24l-3 20H11z"/><path d="M14 14c0-5 3-8 6-8s6 3 6 8"/></svg></span>
      <h4>48 Hour Chiropractic<br>Nutrition Certificate</h4>
    </div>
    <div class="card" style="left:745px;top:171px">
      <span class="ico"><svg width="40" height="40" viewBox="0 0 40 40" fill="none" stroke="#0b5bd3" stroke-width="2"><path d="M20 6c-7 0-12 5-12 12 0 8 12 16 12 16s12-8 12-16c0-7-5-12-12-12z"/><circle cx="20" cy="17" r="4"/></svg></span>
      <h4>24 Hour Chiropractic<br>Pediatrics Certificate</h4>
    </div>
    <div class="card" style="left:146px;top:404px">
      <span class="ico"><svg width="40" height="40" viewBox="0 0 40 40" fill="none" stroke="#0b5bd3" stroke-width="2"><rect x="9" y="6" width="22" height="28" rx="3"/><path d="M20 11v18M14 15h12M14 20h12M14 25h12"/></svg></span>
      <h4>24 Hour Chiropractic<br>Radiology Certificate</h4>
    </div>
    <div class="card" style="left:446px;top:404px">
      <span class="ico"><svg width="40" height="40" viewBox="0 0 40 40" fill="none" stroke="#0b5bd3" stroke-width="2"><circle cx="26" cy="8" r="3"/><path d="M10 18l8-6 6 4-4 8 6 6M18 24l-8 10M24 16l6 4"/></svg></span>
      <h4>48 Hour Chiropractic<br>Sports Medicine Certificate</h4>
    </div>
    <div class="card" style="left:746px;top:404px">
      <span class="ico"><svg width="40" height="40" viewBox="0 0 40 40" fill="none" stroke="#0b5bd3" stroke-width="2"><path d="M6 20L20 8l14 12M10 17v16h20V17"/><circle cx="20" cy="24" r="5"/><path d="M20 21v6M17 24h6"/></svg></span>
      <h4>24 Hour Certified Chiropractic<br>Clinical Assistant</h4>
    </div>
  </div>
</section>

<section class="program">
  <div class="program-bg" role="img" aria-label="Soft blue backdrop of a clinician at work"></div>
  <h2>Online <strong>Certificate Program</strong></h2>
  <p>VROLPWORKSHOPS has made it possible for you to achieve advanced certification in topics relevant to your clinical practice.</p>
  <a class="btn btn-white" href="#">Get Started</a>
</section>

<footer class="footer">
  <div class="f-contact">
    <h4>Contact VROLP Workshops</h4><div class="mini"></div>
    <p>Chiropractic CE Registration &amp; Questions:</p>
    <p class="phone">(555) 014-2286</p>
  </div>
  <div class="f-links">
    <h4>Online Chiropractic CE</h4><div class="mini"></div>
    <ul>
      <li><a href="#">Home</a></li><li><a href="#">Testimonials</a></li>
      <li><a href="#">Courses</a></li><li><a href="#">State Approvals</a></li>
      <li><a href="#">Certification Programs</a></li><li><a href="#">Contact Us</a></li>
      <li><a href="#">Meet the Faculty</a></li><li><a href="#">FAQs</a></li>
    </ul>
  </div>
  <form class="login">
    <h4>Student Login</h4><div class="mini"></div>
    <input type="text" placeholder="Email">
    <input type="password" value="password">
    <button type="button">LOGIN</button>
    <a href="#">Forgot Username or Password?</a>
  </form>
  <p class="copyright">© 2021 Company Name | All Rights Reserved</p>
</footer>

</body>
</html>
```